Plantwise Mechanics Partners. Needs a Business Card Design

We need a business card design for an engineering company which supplies industrial components (pumps, compressors, mechanical seals) provides repairs and services for above mentioned equipments. We offer a uniqe engineering solutions which help our customers to increase the productivness of their manufacturings, and energy savings.

Target Market(s)

Chemical and energy plants, refineries. Food industry and private consumers in a less.

Industry/Entity Type

Business

Contact Information for Business Card

Stylish and sleek design oriented on industrial area.

Requirements
Should not have
• company name shortening

```html
<!DOCTYPE html>
<html lang="en">
<head>
<meta charset="utf-8">
<title>Plantwise Mechanics Partners – Business Card</title>
<link rel="stylesheet" href="https://fonts.googleapis.com/css2?family=Ubuntu:wght@400;500;700&display=swap">
<style>
  :root {
    --page-bg: #e6e7ea;
    --card-white: #f7f7f7;
    --brand-blue: #1f4fb8;
    --brand-blue-light: #2a62cf;
    --accent-red: #e4493b;
    --accent-yellow: #f2b531;
    --ink: #1b1b1b;
    --ink-soft: #333;
  }
  * { box-sizing: border-box; margin: 0; padding: 0; }
  html, body { width: 1200px; height: 780px; overflow: hidden; }
  body {
    background: var(--page-bg);
    font-family: "Ubuntu", sans-serif;
    display: flex;
    align-items: center;
    justify-content: center;
    gap: 40px;
  }
  .card {
    position: relative;
    width: 540px;
    height: 310px;
    overflow: hidden;
    box-shadow: 0 6px 18px rgba(0,0,0,.18);
  }
  .card--front { background: var(--card-white); }
  .card--back { background: var(--brand-blue); }

  .line, .band { position: absolute; left: 0; right: 0; }
  .brand-disc { position: absolute; border-radius: 50%; }
  .company-name {
    position: absolute;
    font-weight: 700;
    font-size: 22px;
    line-height: 1.2;
    white-space: nowrap;
  }

  /* front */
  .front__rule-top { top: 26px; height: 2px; background: var(--accent-red); }
  .front__band-top { top: 34px; height: 70px; background: var(--brand-blue); }
  .front__rule-mid { top: 110px; height: 2px; background: var(--accent-red); }
  .front__band-bottom { top: 288px; bottom: 0; background: var(--brand-blue); }
  .card--front .brand-disc {
    left: 56px; top: 40px; width: 104px; height: 104px;
    background: var(--card-white);
  }
  .card--front .company-name { left: 174px; top: 120px; color: var(--ink); }

  .person { position: absolute; left: 40px; top: 196px; width: 196px; text-align: right; }
  .person__name { font-weight: 700; font-size: 20px; color: var(--brand-blue); }
  .person__role { font-size: 14px; color: var(--ink-soft); margin-top: 2px; }
  .divider { position: absolute; left: 252px; top: 178px; width: 2px; height: 78px; background: var(--accent-red); }

  .contacts { position: absolute; left: 270px; top: 180px; list-style: none; }
  .contacts li { display: flex; align-items: center; gap: 8px; font-size: 14px; color: var(--ink); height: 25px; }
  .contacts svg { width: 17px; height: 17px; flex: none; }

  /* back */
  .back__rule-top { top: 18px; height: 2px; background: var(--card-white); }
  .back__band-top { top: 26px; height: 70px; background: var(--card-white); }
  .back__inner-rule { top: 34px; height: 2px; background: var(--brand-blue); }
  .card--back .brand-disc {
    left: 418px; top: 46px; width: 96px; height: 96px;
    background: var(--brand-blue-light);
    border: 4px solid var(--card-white);
  }
  .card--back .company-name { left: 44px; top: 108px; color: var(--card-white); }
  .offer { position: absolute; left: 44px; top: 170px; color: var(--card-white); }
  .offer__title { font-size: 16px; font-weight: 500; letter-spacing: .6px; }
  .offer__list { font-size: 13px; margin-top: 12px; opacity: .92; }
  .back__band-bottom { top: 252px; height: 36px; background: var(--card-white); }
  .back__rule-bottom { top: 294px; height: 2px; background: var(--card-white); }
</style>
</head>
<body>
  <section class="card card--front" aria-label="Business card front">
    <div class="line front__rule-top"></div>
    <div class="band front__band-top"></div>
    <div class="line front__rule-mid"></div>
    <div class="brand-disc"></div>
    <div class="company-name">Plantwise Mechanics Partners</div>

    <div class="person">
      <div class="person__name">Employee Name</div>
      <div class="person__role">Manager</div>
    </div>
    <div class="divider"></div>
    <ul class="contacts">
      <li>
        <svg viewBox="0 0 16 16"><rect width="16" height="16" rx="3" fill="var(--accent-red)"/><path d="M5 3.5l2 2-1 1.2c.6 1.3 1.6 2.3 2.9 2.9l1.2-1 2 2-1.2 1.4C7.8 11.8 4.2 8.2 3.6 5z" fill="#fff"/></svg>
        0123 555 780
      </li>
      <li>
        <svg viewBox="0 0 16 16"><rect width="16" height="16" rx="3" fill="var(--brand-blue-light)"/><rect x="3.5" y="5" width="9" height="6.5" fill="none" stroke="#fff" stroke-width="1.2"/><path d="M3.5 5l4.5 3.5L12.5 5" fill="none" stroke="#fff" stroke-width="1.2"/></svg>
        hello@plantwisemech.net.nz
      </li>
      <li>
        <svg viewBox="0 0 16 16"><rect width="16" height="16" rx="3" fill="var(--accent-yellow)"/><circle cx="8" cy="8" r="4.5" fill="none" stroke="#fff" stroke-width="1.1"/><path d="M3.5 8h9M8 3.5c-2 2.5-2 6.5 0 9M8 3.5c2 2.5 2 6.5 0 9" fill="none" stroke="#fff" stroke-width="1"/></svg>
        www.plantwisemech.co.nz
      </li>
    </ul>

    <div class="band front__band-bottom"></div>
  </section>

  <section class="card card--back" aria-label="Business card back">
    <div class="line back__rule-top"></div>
    <div class="band back__band-top"></div>
    <div class="line back__inner-rule"></div>
    <div class="brand-disc"></div>
    <div class="company-name">Plantwise Mechanics Partners</div>

    <div class="offer">
      <div class="offer__title">OUR OFFERED GOODS AND SERVICES</div>
      <div class="offer__list">pump equipment | sealing solutions | compressor components | services</div>
    </div>

    <div class="band back__band-bottom"></div>
    <div class="line back__rule-bottom"></div>
  </section>
</body>
</html>
```